Brightwell Building Group Stationary Revamp

We need a full set of new stationary including business cards for our Public Sector Construction company based in the South East of England. We have a new logo (attached) that we want to launch and revamp all of our company literature. We are required to send a lot of correspondence to residents etc so a consistent theme is required across everything. Also attached is our existing templates.

Target Market(s)

We work for Council and government provided housing organisations and NOT private individuals. All of our clients represent government spent money, so we need to look professional and instantly recognisable brand.

Industry/Entity Type

Business

Colors

Designer to choose colors to be used in the design.

Requirements
Must have
• New fresh designs that utilise our new logo. And the letterhead needs to be able to be rolled out onto a word template so that all staff can type straight onto it rather than us having to have it printed first.
Nice to have
• I am looking forward to seeing your best efforts as designers.

```html
<!DOCTYPE html>
<html lang="en">
<head>
<meta charset="utf-8">
<title>Brightwell Building Group – Presentation Folder</title>
<link href="https://fonts.googleapis.com/css2?family=Questrial&display=swap" rel="stylesheet">
<style>
  :root {
    --backdrop: #b9b9b9;
    --gold-light: #e6c21a;
    --gold-mid: #c9a010;
    --gold-deep: #8f6e06;
    --ink-brown: #231816;
    --paper: #ffffff;
    --paper-shade: #ececec;
    --text-light: #e9e4df;
    --name-ink: #2a2220;
  }
  * { margin: 0; padding: 0; box-sizing: border-box; }
  html, body {
    width: 1200px; height: 814px; overflow: hidden;
    background: var(--backdrop);
    font-family: "Questrial", sans-serif;
  }
  .folder-spread {
    position: absolute; left: 140px; top: 97px;
    width: 920px; height: 620px;
    display: flex;
    box-shadow: 0 12px 30px rgba(0,0,0,0.28);
  }
  .folder-panel { position: relative; width: 460px; height: 620px; overflow: hidden; }
  .folder-panel svg.panel-art { position: absolute; inset: 0; }
  .back-watermark {
    position: absolute; left: 0; right: 0; top: 210px;
    text-align: center; font-size: 30px; color: rgba(150, 112, 8, 0.45);
    letter-spacing: 0.5px;
  }
  .contact-block {
    position: absolute; left: 42px; top: 486px;
    color: var(--text-light); font-size: 11.5px; line-height: 14px;
  }
  .contact-block .address { margin-bottom: 6px; }
  .contact-list { list-style: none; }
  .contact-list li { display: flex; align-items: center; gap: 8px; height: 14px; }
  .contact-list svg { width: 10px; height: 10px; fill: var(--gold-light); flex-shrink: 0; }
  .front-brand {
    position: absolute; left: 0; right: 0; top: 232px;
    text-align: center; font-size: 27px; color: var(--name-ink);
  }
</style>
</head>
<body>
  <main class="folder-spread">
    <section class="folder-panel folder-back">
      <svg class="panel-art" viewBox="0 0 460 620" aria-hidden="true">
        <defs>
          <radialGradient id="goldGlow" cx="0.45" cy="0.45" r="0.8">
            <stop offset="0" stop-color="var(--gold-light)"/>
            <stop offset="0.55" stop-color="var(--gold-mid)"/>
            <stop offset="1" stop-color="var(--gold-deep)"/>
          </radialGradient>
        </defs>
        <rect width="460" height="620" fill="url(#goldGlow)"/>
        <path d="M0 442 Q230 510 460 428 L460 440 Q230 515 0 446 Z" fill="var(--paper-shade)"/>
        <path d="M0 446 Q230 515 460 440 L460 620 L0 620 Z" fill="var(--ink-brown)"/>
      </svg>
      <div class="back-watermark">Brightwell Building Group</div>
      <div class="contact-block">
        <p class="address">Harrow Court<br>12 Lindfield Avenue<br>Ashford, Kent, TN23 4QX<br>Reg No: 07318254</p>
        <ul class="contact-list">
          <li><svg viewBox="0 0 10 10"><path d="M2 0 L4 2.5 L3 4 Q4.5 6 6 7 L7.5 6 L10 8 L8.5 10 Q3 9 0 2 Z"/></svg>020 7946 0812</li>
          <li><svg viewBox="0 0 10 10"><rect x="2" y="0" width="6" height="3"/><rect x="0" y="3.5" width="10" height="4.5" rx="1"/><rect x="2" y="8.5" width="6" height="1.5"/></svg>020 7946 0813</li>
          <li><svg viewBox="0 0 10 10"><path d="M0 2 H10 V8 H0 Z M0.5 2.5 L5 5.5 L9.5 2.5" stroke="var(--ink-brown)" stroke-width="0.8"/></svg>info@brightwellgroup.co.uk</li>
          <li><svg viewBox="0 0 10 10"><circle cx="5" cy="5" r="5"/></svg>www.brightwellgroup.co.uk</li>
        </ul>
      </div>
    </section>
    <section class="folder-panel folder-front">
      <svg class="panel-art" viewBox="0 0 460 620" aria-hidden="true">
        <defs>
          <linearGradient id="paperSheen" x1="0" y1="0" x2="1" y2="1">
            <stop offset="0" stop-color="var(--paper-shade)"/>
            <stop offset="0.5" stop-color="var(--paper)"/>
            <stop offset="1" stop-color="var(--paper-shade)"/>
          </linearGradient>
        </defs>
        <rect width="460" height="620" fill="url(#paperSheen)"/>
        <path d="M0 446 Q260 445 460 292 L460 300 Q260 458 0 462 Z" fill="var(--gold-mid)"/>
        <path d="M0 462 Q260 458 460 300 L460 620 L0 620 Z" fill="var(--ink-brown)"/>
      </svg>
      <div class="front-brand">Brightwell Building Group</div>
    </section>
  </main>
</body>
</html>
```